Flyer-Design für Mittagsbelieferung
Zielgruppe
Mittags Belieferung ältere Menschen, Firmen, Berufstätige
Aufgabenstellung
Text aus Datei den Bestellzettel nicht weiter beachten nur Seite 2 u.3... Logo vielleicht vorne drauf... Format bin ich unentschieden

```html
<!DOCTYPE html>
<html lang="de">
<head>
<meta charset="utf-8">
<title>Pilvo – Mittagsbelieferung</title>
<link rel="stylesheet" href="https://fonts.googleapis.com/css2?family=Oswald:wght@400;500&family=Barlow:wght@400;500&display=swap">
<style>
  :root {
    --red: #c3171b;
    --yellow: #f9b200;
    --orange: #f07a1e;
    --white: #ffffff;
    --ink: #1a1a1a;
  }
  * { margin: 0; padding: 0; box-sizing: border-box; }
  html, body { width: 1131px; height: 1200px; overflow: hidden; background: #fff; }
  .flyer { position: relative; width: 1131px; height: 1200px; overflow: hidden; font-family: "Barlow", sans-serif; color: var(--white); }
  .abs { position: absolute; }

  /* left column */
  .area-header { left: 0; top: 0; width: 566px; height: 110px; background: var(--red); }
  .area-header h2 { position: absolute; left: 35px; top: 38px; font: 400 40px/1 "Oswald", sans-serif; letter-spacing: -0.3px; white-space: nowrap; }
  .area-panel { left: 0; top: 110px; width: 566px; height: 250px; background: linear-gradient(180deg, #2e2e2e, #232323); }
  .service-badge { left: 34px; top: 134px; width: 137px; height: 137px; background: var(--yellow); display: flex; align-items: center; justify-content: center; }
  .town-list { top: 124px; font-size: 23px; line-height: 32.5px; list-style: none; letter-spacing: 0.3px; }
  .town-list.col-a { left: 206px; }
  .town-list.col-b { left: 362px; }

  .photo-customer { left: 0; top: 360px; width: 566px; height: 420px; background: radial-gradient(ellipse at 45% 45%, #b49a7c 0%, #5d4b3a 45%, #1f2228 100%); }
  .lower-panel { left: 0; top: 780px; width: 566px; height: 420px; background: linear-gradient(180deg, #262626, #1b1b1b); }
  .leaf-art { left: 270px; top: 845px; width: 296px; height: 355px; background: radial-gradient(ellipse at 60% 55%, #5e9a2f 0%, #3c6f1c 55%, rgba(40,70,20,0) 75%); }
  .dash { height: 0; border-top: 2px dashed rgba(255,255,255,0.85); }

  .name-disc { left: 368px; top: 697px; width: 174px; height: 174px; border-radius: 50%; background: var(--white); display: flex; align-items: center; justify-content: center; }
  .name-disc span { font: 500 34px/1 "Oswald", sans-serif; color: var(--red); }

  .contact-block { left: 37px; top: 812px; font-size: 22px; line-height: 32.5px; }
  .contact-block h3 { font: 400 41px/1.15 "Oswald", sans-serif; display: flex; align-items: center; gap: 8px; margin-bottom: 4px; transform: scaleX(0.9); transform-origin: left; }
  .tag { display: inline-block; background: var(--red); padding: 0 6px; line-height: 30px; margin-top: 6px; }
  .hours-block { left: 37px; top: 1024px; font-size: 22px; line-height: 33px; }

  /* right column */
  .photo-courier { left: 566px; top: 0; width: 565px; height: 890px; background: linear-gradient(135deg, #0d0d0f 0%, #1b1b1d 35%, #5a2a22 60%, #d8482e 85%, #b53722 100%); }
  .brand-mark { left: 600px; top: 40px; display: flex; align-items: center; gap: 14px; }
  .brand-mark .dot { width: 64px; height: 64px; border-radius: 50%; background: var(--orange); }
  .brand-mark .name { font: 500 56px/1 "Oswald", sans-serif; color: var(--white); }
  .hero-contact { left: 600px; top: 233px; font: 400 44px/52px "Oswald", sans-serif; transform: scaleX(0.88); transform-origin: left; white-space: nowrap; }

  .offer-band { left: 566px; top: 890px; width: 565px; height: 174px; background: var(--red); }
  .offer-band h1 { position: absolute; left: 34px; top: 25px; font: 500 58px/1 "Oswald", sans-serif; transform: scaleX(0.85); transform-origin: left; white-space: nowrap; }
  .offer-band p { position: absolute; left: 34px; top: 94px; font: 500 41px/1 "Oswald", sans-serif; transform: scaleX(0.82); transform-origin: left; white-space: nowrap; }
  .price { left: 923px; top: 841px; width: 128px; height: 128px; border-radius: 50%; background: var(--white); color: var(--ink); display: flex; align-items: center; justify-content: center; font: 500 46px/1 "Oswald", sans-serif; }
  .info-band { left: 566px; top: 1064px; width: 565px; height: 136px; background: var(--yellow); color: var(--ink); }
  .info-band p { position: absolute; left: 34px; font-size: 22px; line-height: 34px; }
</style>
</head>
<body>
<div class="flyer">
  <!-- left column -->
  <div class="abs area-header"><h2>Derzeitiges Auslieferungsgebiet:</h2></div>
  <div class="abs area-panel"></div>
  <div class="abs service-badge">
    <svg width="70" height="70" viewBox="0 0 70 70" fill="none" stroke="#fff" stroke-width="5" stroke-linecap="round" stroke-linejoin="round">
      <path d="M14 36l14 14 28-30"/>
    </svg>
  </div>
  <ul class="abs town-list col-a">
    <li>Gägelow</li><li>Proseken</li><li>Barnekow</li><li>Zierow</li><li>Gressow</li><li>Stofferdorf</li>
  </ul>
  <ul class="abs town-list col-b">
    <li>Woltersdorf</li><li>Wismar</li><li>Neuburg</li><li>Hornstorf</li><li>Kritzow</li><li>Weitere möglich!</li>
  </ul>

  <div class="abs photo-customer" role="img" aria-label="Foto: lächelnde Frau packt Essen aus einer Papiertüte auf dem Sofa aus"></div>
  <div class="abs lower-panel"></div>
  <div class="abs leaf-art" role="img" aria-label="Foto: frische Rucolablätter"></div>
  <div class="abs dash" style="left:0;top:360px;width:566px"></div>
  <div class="abs dash" style="left:0;top:780px;width:566px"></div>

  <div class="abs contact-block">
    <h3>Pilvo-Restaurant
      <svg width="34" height="44" viewBox="0 0 34 44"><path d="M17 2C8.7 2 2 8.6 2 16.8 2 28 17 42 17 42s15-14 15-25.2C32 8.6 25.3 2 17 2z" fill="var(--orange)"/><circle cx="17" cy="17" r="6" fill="#222"/></svg>
    </h3>
    <p>Lindenweg 14</p>
    <p>23968 Gägelow</p>
    <p>Tel.: 03841/5518720</p>
    <p>E-Mail: pilvo@postfach-mail.de</p>
  </div>
  <div class="abs hours-block">
    <span class="tag">Lieferung:</span><br>
    Mo. – Sa. 10.30 – 12.30 Uhr<br>
    <span class="tag">An-und Abbestellungen:</span><br>
    bis 10.00 Uhr
  </div>

  <div class="abs name-disc"><span>pilvo</span></div>

  <!-- right column -->
  <div class="abs photo-courier" role="img" aria-label="Foto: lächelnder Lieferfahrer in roter Weste mit roter Thermotasche"></div>
  <div class="abs brand-mark"><span class="dot"></span><span class="name">pilvo</span></div>
  <div class="abs hero-contact">
    <p>Tel: 03841 / 55 18 720</p>
    <p>E-Mail: pilvo@postfach-mail.de</p>
  </div>

  <div class="abs offer-band">
    <h1>Ihr Wunschmenü</h1>
    <p>inkl. Nachtisch und Lieferung</p>
  </div>
  <div class="abs dash" style="left:566px;top:890px;width:565px"></div>
  <div class="abs price">6,00€</div>
  <div class="abs info-band">
    <p style="top:26px">Lieferung: Mo. – Sa. 10.30 – 12.30 Uhr</p>
    <p style="top:60px">An-und Abbestellungen: bis 10.00 Uhr</p>
  </div>
</div>
</body>
</html>
```